Harborline Security and Surveillance Business Card

Business Card Design - Company Name:Freedom Security and SurveillanceWe are a Security Systems Integrator Specializing in Security Systems/ Video Surveillance and Access Control. Our areas of expertise are:Security SystemsVideo SurveillanceAccess ControlFire Alarm SystemsNetwork CablingCellular BoostersMy input is the Front of the Card is: logo, name of Business, My Name, Phone Number, and email.Rear of Card is the 6 areas of expertise, I just dont want the front to be very busy.
Name: Tom Jenner
Title: President
Email: tom@harborlinesecuritysys.example
website: harborlinesecuritysys.example

```html
<!DOCTYPE html>
<html lang="en">
<head>
<meta charset="utf-8">
<title>Harborline Security and Surveillance Business Card</title>
<link rel="stylesheet" href="https://fonts.googleapis.com/css2?family=Lato:wght@400;700&display=swap">
<style>
  :root {
    --brand-blue: #1656c2;
    --ink: #3d3f44;
    --ink-soft: #55585e;
    --paper: #ffffff;
    --backdrop: #6e7a86;
    --tick: #f2b632;
    --rule: #d9dce1;
  }
  * { box-sizing: border-box; margin: 0; padding: 0; }
  html, body {
    width: 1200px; height: 978px; overflow: hidden;
    background: var(--backdrop);
    font-family: "Lato", sans-serif;
  }
  .stage { position: relative; width: 1200px; height: 978px; }
  .card {
    position: absolute; left: 228px; width: 744px; height: 424px;
    background: var(--paper);
    box-shadow: 0 6px 18px rgba(0,0,0,0.35);
    overflow: hidden;
  }
  .card--front { top: 38px; }
  .card--back { top: 490px; }

  /* front */
  .name-tab {
    position: absolute; left: 396px; top: 68px; width: 348px; height: 96px;
    background: var(--brand-blue);
    clip-path: polygon(0 0, 100% 0, 100% 100%, 13% 100%);
    color: var(--paper); text-align: right; padding: 14px 50px 0 0;
  }
  .name-tab__name { font-weight: 700; font-size: 34px; line-height: 40px; letter-spacing: 0.5px; }
  .name-tab__title { font-size: 19px; line-height: 24px; letter-spacing: 0.5px; }

  .front-brand {
    position: absolute; left: 40px; top: 282px; width: 290px;
    display: flex; align-items: center; gap: 12px;
  }
  .brand-dot { flex: none; width: 26px; height: 26px; border-radius: 50%; background: var(--brand-blue); }
  .brand-name {
    color: var(--brand-blue); font-weight: 700; text-transform: uppercase;
    letter-spacing: 1.5px;
  }
  .front-brand .brand-name { font-size: 18px; line-height: 23px; }

  .front-divider {
    position: absolute; left: 346px; top: 262px; width: 2px; height: 138px;
    background: linear-gradient(to bottom, transparent, #c9cdd3 20%, #c9cdd3 80%, transparent);
  }
  .contact {
    position: absolute; right: 50px; top: 258px; text-align: right; list-style: none;
  }
  .contact__company { font-weight: 700; font-size: 20px; color: var(--ink); line-height: 30px; margin-bottom: 4px; }
  .contact__item {
    display: flex; justify-content: flex-end; align-items: center; gap: 10px;
    font-size: 20px; color: var(--ink-soft); line-height: 34px;
  }
  .contact__item svg { width: 17px; height: 17px; fill: var(--brand-blue); flex: none; }

  /* back */
  .back-brand {
    position: absolute; left: 0; right: 0; top: 100px;
    display: flex; justify-content: center; align-items: center; gap: 16px;
  }
  .back-brand .brand-dot { width: 40px; height: 40px; }
  .back-brand .brand-name { font-size: 28px; letter-spacing: 2px; }

  .services {
    position: absolute; left: 0; bottom: 0; width: 744px; height: 182px;
    background: var(--brand-blue);
  }
  .services__list {
    position: absolute; top: 34px; list-style: none;
  }
  .services__list--left { left: 108px; }
  .services__list--right { left: 444px; }
  .services__item {
    display: flex; align-items: center; gap: 10px;
    color: var(--paper); font-size: 20px; line-height: 36px;
  }
  .services__item svg { width: 20px; height: 20px; flex: none; }
  .services__divider {
    position: absolute; left: 371px; top: 24px; width: 1px; height: 128px;
    background: rgba(255,255,255,0.7);
  }
</style>
</head>
<body>
<main class="stage">

  <section class="card card--front" aria-label="Card front">
    <div class="name-tab">
      <div class="name-tab__name">TOM JENNER</div>
      <div class="name-tab__title">PRESIDENT</div>
    </div>

    <div class="front-brand">
      <span class="brand-dot"></span>
      <span class="brand-name">Harborline Security and Surveillance</span>
    </div>

    <div class="front-divider"></div>

    <ul class="contact">
      <li class="contact__company">Harborline Security and Surveillance</li>
      <li class="contact__item">555.014.2276
        <svg viewBox="0 0 24 24" aria-hidden="true"><path d="M6.6 10.8a15.1 15.1 0 0 0 6.6 6.6l2.2-2.2c.3-.3.7-.4 1-.2 1.1.4 2.3.6 3.6.6.6 0 1 .4 1 1V20c0 .6-.4 1-1 1A17 17 0 0 1 3 4c0-.6.4-1 1-1h3.5c.6 0 1 .4 1 1 0 1.3.2 2.5.6 3.6.1.3 0 .7-.2 1z"/></svg>
      </li>
      <li class="contact__item">tom@harborlinesecuritysys.example
        <svg viewBox="0 0 24 24" aria-hidden="true"><path d="M2 5h20v3l-10 6L2 8z M2 10.3l10 6 10-6V19H2z"/></svg>
      </li>
      <li class="contact__item">harborlinesecuritysys.example
        <svg viewBox="0 0 24 24" aria-hidden="true"><path d="M12 2a10 10 0 1 0 0 20 10 10 0 0 0 0-20zm6.9 9h-3a15 15 0 0 0-1.3-5.6A8 8 0 0 1 18.9 11zM12 4.1c.9 1.2 1.8 3.6 2 6.9h-4c.2-3.3 1.1-5.7 2-6.9zM9.4 5.4A15 15 0 0 0 8.1 11h-3a8 8 0 0 1 4.3-5.6zM5.1 13h3a15 15 0 0 0 1.3 5.6A8 8 0 0 1 5.1 13zm6.9 6.9c-.9-1.2-1.8-3.6-2-6.9h4c-.2 3.3-1.1 5.7-2 6.9zm2.6-1.3a15 15 0 0 0 1.3-5.6h3a8 8 0 0 1-4.3 5.6z"/></svg>
      </li>
    </ul>
  </section>

  <section class="card card--back" aria-label="Card back">
    <div class="back-brand">
      <span class="brand-dot"></span>
      <span class="brand-name">Harborline Security and Surveillance</span>
    </div>

    <div class="services">
      <ul class="services__list services__list--left">
        <li class="services__item"><svg viewBox="0 0 20 20" aria-hidden="true"><rect x="1.5" y="3.5" width="14" height="14" fill="none" stroke="#fff" stroke-width="1.5"/><path d="M4.5 10l3.5 3.5L18 2.5" fill="none" stroke="var(--tick)" stroke-width="3" stroke-linecap="round" stroke-linejoin="round"/></svg>Security Systems</li>
        <li class="services__item"><svg viewBox="0 0 20 20" aria-hidden="true"><rect x="1.5" y="3.5" width="14" height="14" fill="none" stroke="#fff" stroke-width="1.5"/><path d="M4.5 10l3.5 3.5L18 2.5" fill="none" stroke="var(--tick)" stroke-width="3" stroke-linecap="round" stroke-linejoin="round"/></svg>Video Surveillance</li>
        <li class="services__item"><svg viewBox="0 0 20 20" aria-hidden="true"><rect x="1.5" y="3.5" width="14" height="14" fill="none" stroke="#fff" stroke-width="1.5"/><path d="M4.5 10l3.5 3.5L18 2.5" fill="none" stroke="var(--tick)" stroke-width="3" stroke-linecap="round" stroke-linejoin="round"/></svg>Access Control</li>
      </ul>
      <div class="services__divider"></div>
      <ul class="services__list services__list--right">
        <li class="services__item"><svg viewBox="0 0 20 20" aria-hidden="true"><rect x="1.5" y="3.5" width="14" height="14" fill="none" stroke="#fff" stroke-width="1.5"/><path d="M4.5 10l3.5 3.5L18 2.5" fill="none" stroke="var(--tick)" stroke-width="3" stroke-linecap="round" stroke-linejoin="round"/></svg>Fire Alarm Systems</li>
        <li class="services__item"><svg viewBox="0 0 20 20" aria-hidden="true"><rect x="1.5" y="3.5" width="14" height="14" fill="none" stroke="#fff" stroke-width="1.5"/><path d="M4.5 10l3.5 3.5L18 2.5" fill="none" stroke="var(--tick)" stroke-width="3" stroke-linecap="round" stroke-linejoin="round"/></svg>Network Cabling</li>
        <li class="services__item"><svg viewBox="0 0 20 20" aria-hidden="true"><rect x="1.5" y="3.5" width="14" height="14" fill="none" stroke="#fff" stroke-width="1.5"/><path d="M4.5 10l3.5 3.5L18 2.5" fill="none" stroke="var(--tick)" stroke-width="3" stroke-linecap="round" stroke-linejoin="round"/></svg>Cellular Boosters</li>
      </ul>
    </div>
  </section>

</main>
</body>
</html>
```